Email Marketing for HR and Career Consulting Company

I am looking for a email marketing template that will be developed in HTML format. Right now, we need PSD file format.

The content will include:

1. Featured / Poplar Blog post
2. Latest blog post this week
3. Latest jobs this week
4. Connect with us (social media)

This is a bi-weekly template which we will be sending to people who sign up our weekly newsletter. The purpose of the newsletter is to provide career advise and also latest jobs that's available from our company so that we can redirect them to our career page or apply to our latest jobs.
Updates

Project Deadline Extended
Reason: I am extending this deadline as I would like to see more designs. So far, I have only shortlisted one design that is close to what I am looking for. To all designers, please note that your design would have to be practical and easy to navigate. It also must take into consideration that when we develop this into html, it will b responsive.

Target Market(s)

Job seekers - age group 25 - 45

Industry/Entity Type

Consulting

Font styles to use
Other font styles liked:
• Helvetical

Colors
0492cd
e34197
ec1f27
85cae6
33a6d7
85acd3
eda3c7
e667a6
f59195

Requirements
Must have
• 1. Social media icons
• 2. Links - jobs, contact us
• 3. Popular career advice
• 4. Latest career advice
• 5. Featured jobs
• 6. Popular jobs
Nice to have
• I would like to see clean and minimalist design. Please try to avoid black color. Use pastel colors as much as possible. Our website is www.careerpondly.com.sg
Should not have
• Should avoid black and dark colors

```html
<!DOCTYPE html>
<html lang="en">
<head>
<meta charset="utf-8">
<title>Careerpondly Newsletter</title>
<link rel="stylesheet" href="https://fonts.googleapis.com/css2?family=Roboto:wght@400;500&display=swap">
<style>
  :root {
    --page-bg: #eef1f4;
    --panel-bg: #ffffff;
    --panel-line: #dfe3e8;
    --brand-blue: #0492cd;
    --button-blue: #1a9ad6;
    --text-main: #3a3f44;
    --text-body: #5a5f64;
    --text-label: #a3a8ad;
    --soft-row: #f6f7f8;
    --icon-red: #ec1f27;
    --trophy-purple: #9b3fb5;
    --star-green: #8cc964;
    --heart-pink: #f0467a;
    --photo-tone-a: #c9ced6;
    --photo-tone-b: #7f8895;
    --hero-tone-a: #2f6fae;
    --hero-tone-b: #bcd8ee;
  }
  * { box-sizing: border-box; margin: 0; padding: 0; }
  html, body { width: 1200px; height: 1200px; overflow: hidden; }
  body {
    background: var(--page-bg);
    font-family: "Roboto", Helvetica, Arial, sans-serif;
    color: var(--text-main);
    display: flex;
    justify-content: center;
    align-items: center;
    gap: 30px;
  }
  .email-panel {
    width: 360px;
    height: 900px;
    background: var(--panel-bg);
    border: 1px solid var(--panel-line);
    overflow: hidden;
    display: flex;
    flex-direction: column;
  }
  .section-icon {
    width: 74px; height: 74px; border-radius: 50%;
    display: flex; align-items: center; justify-content: center;
    margin: 28px auto 0;
  }
  .section-icon svg { width: 38px; height: 38px; fill: #fff; }
  .icon-trophy { background: var(--trophy-purple); }
  .icon-star { background: var(--star-green); }
  .icon-heart { background: var(--heart-pink); }
  .section-label {
    text-align: center; font-size: 13px; letter-spacing: .5px;
    color: var(--text-label); margin-top: 20px; text-transform: uppercase;
  }
  .section-title {
    text-align: center; font-size: 21px; font-weight: 500;
    line-height: 1.6; margin: 12px 22px 0; color: var(--text-main);
  }
  .section-text {
    text-align: center; font-size: 12.5px; line-height: 2.15;
    color: var(--text-body); margin: 16px 24px 0;
  }
  .job-meta {
    display: flex; justify-content: center; gap: 18px;
    font-size: 11px; color: var(--text-body); margin-top: 18px;
  }
  .job-meta span { display: flex; align-items: center; gap: 5px; }
  .job-meta svg { width: 10px; height: 10px; fill: var(--icon-red); }

  /* featured job */
  .team-photo {
    height: 180px;
    background: linear-gradient(160deg, var(--photo-tone-a), var(--photo-tone-b));
  }
  .challenges { margin: 32px 22px 0; font-size: 12px; color: var(--text-body); }
  .challenges h3 { font-size: 13px; font-weight: 500; color: var(--text-main); margin-bottom: 12px; }
  .challenges li { list-style: none; line-height: 1.5; margin-bottom: 14px; }

  /* career advice */
  .brand-header {
    height: 92px; display: flex; align-items: center; justify-content: center; gap: 8px;
  }
  .brand-dot { width: 14px; height: 14px; border-radius: 50%; background: var(--brand-blue); }
  .brand-name { font-size: 17px; font-weight: 500; color: var(--brand-blue); }
  .hero-image {
    height: 200px;
    background: linear-gradient(135deg, var(--hero-tone-a), var(--hero-tone-b));
  }
  .read-button {
    display: block; margin: 26px auto 0; width: 220px; height: 38px;
    background: var(--button-blue); color: #fff; font-size: 15px; font-weight: 500;
    text-align: center; line-height: 38px; text-decoration: none;
  }

  /* popular jobs */
  .popular-head { padding-bottom: 24px; }
  .job-row { padding: 20px 22px 18px; }
  .job-row:nth-child(odd) { background: var(--soft-row); }
  .job-row h4 { font-size: 13.5px; font-weight: 400; line-height: 1.45; color: var(--text-main); }
  .job-row .job-meta { justify-content: space-between; margin-top: 12px; gap: 6px; }
  .apply-button {
    display: block; margin: 14px auto 0; width: 130px; height: 34px;
    border: 1.5px solid var(--brand-blue); border-radius: 3px;
    text-align: center; line-height: 31px; font-size: 12px;
    color: var(--text-main); text-decoration: none; background: #fff;
  }
</style>
</head>
<body>

<svg width="0" height="0" style="position:absolute" aria-hidden="true">
  <symbol id="pin" viewBox="0 0 10 10"><path d="M5 0a3.5 3.5 0 0 0-3.5 3.5C1.5 6 5 10 5 10s3.5-4 3.5-6.5A3.5 3.5 0 0 0 5 0zm0 5a1.4 1.4 0 1 1 0-2.8A1.4 1.4 0 0 1 5 5z"/></symbol>
  <symbol id="chat" viewBox="0 0 10 10"><path d="M0 1h6v4H2L0 6.5z"/><path d="M4 6h4l2 2V3H7v3.2H4z"/></symbol>
  <symbol id="hourglass" viewBox="0 0 10 10"><path d="M1 0h8v1H8c0 2-2 3-2 4s2 2 2 4h1v1H1V9h1c0-2 2-3 2-4S2 3 2 1H1z"/></symbol>
</svg>

<!-- Featured job -->
<section class="email-panel featured-job">
  <div class="team-photo" role="img" aria-label="Photo of job candidates in business attire waiting for an interview"></div>
  <div class="section-icon icon-trophy">
    <svg viewBox="0 0 24 24"><path d="M6 2h12v2h3v3a4 4 0 0 1-4 4h-.4A5 5 0 0 1 13 14v3h3v3H8v-3h3v-3a5 5 0 0 1-3.6-3H7a4 4 0 0 1-4-4V4h3zm0 4H5v1a2 2 0 0 0 1 1.7zm12 0v2.7A2 2 0 0 0 19 7V6z"/></svg>
  </div>
  <p class="section-label">Featured Jobs</p>
  <h2 class="section-title">Logistics Manager - Fashion Retail</h2>
  <p class="section-text">Our client has since evolved from a humble beginning as a traditional freight forwarder to a fully integrated logistics solutions provider. This is a new role created and will be in charged of managing a Regional Distribution Centre for their retail customer.</p>
  <div class="job-meta">
    <span><svg><use href="#pin"/></svg>Singapore</span>
    <span><svg><use href="#chat"/></svg>Human Resource</span>
    <span><svg><use href="#hourglass"/></svg>Full time</span>
  </div>
  <div class="challenges">
    <h3>The Challenges</h3>
    <ul>
      <li>Account mamagement with existing account (70%)</li>
      <li>Setup new account (30%)</li>
      <li>Posting jobs on all job boards. Posting jobs on internal applicant tracking system</li>
    </ul>
  </div>
</section>

<!-- Career advice -->
<section class="email-panel career-advice">
  <header class="brand-header">
    <span class="brand-dot"></span>
    <span class="brand-name">Careerpondly</span>
  </header>
  <div class="hero-image" role="img" aria-label="Hand holding a tablet with a job search sketch and magnifying glass"></div>
  <div class="section-icon icon-star">
    <svg viewBox="0 0 24 24"><path d="M12 2l3 6.5 7 .8-5.2 4.8 1.5 7L12 17.5 5.7 21l1.5-7L2 9.3l7-.8z"/></svg>
  </div>
  <p class="section-label">Career Advice Goodness</p>
  <h2 class="section-title">Contract Jobs: Can They Really Be A Career Option?</h2>
  <p class="section-text">Making a career out of contract jobs isn't out of the realm of possibility. While it does involve a lot of work, the payoff, the joy of entrepreneurship, is hard to match. But where to start? How do you keep it going? Last month, I was invited to an event with Brightway Talent to tackle one of the industry's biggest questions: can you make a career out of contract jobs?</p>
  <a class="read-button" href="#">Read Full Article</a>
</section>

<!-- Popular jobs -->
<section class="email-panel popular-jobs">
  <div class="popular-head">
    <div class="section-icon icon-heart">
      <svg viewBox="0 0 24 24"><path d="M12 21l-1.4-1.3C5.4 15 2 12 2 8.3A5 5 0 0 1 7 3.3c1.8 0 3.6.9 5 2.3a6.8 6.8 0 0 1 5-2.3 5 5 0 0 1 5 5c0 3.7-3.4 6.7-8.6 11.4z"/></svg>
    </div>
    <p class="section-label">Popular Jobs</p>
    <h2 class="section-title">Apply for latest jobs this week</h2>
  </div>
  <div class="job-list">
    <div class="job-row">
      <h4>Senior / Recruitment Consultant - Executive Search Division</h4>
      <div class="job-meta">
        <span><svg><use href="#pin"/></svg>Singapore</span>
        <span><svg><use href="#chat"/></svg>Human Resource</span>
        <span><svg><use href="#hourglass"/></svg>Full time</span>
      </div>
      <a class="apply-button" href="#">Apply</a>
    </div>
    <div class="job-row">
      <h4>IS Support Analyst, APAC</h4>
      <div class="job-meta">
        <span><svg><use href="#pin"/></svg>Singapore</span>
        <span><svg><use href="#chat"/></svg>Information Technology</span>
        <span><svg><use href="#hourglass"/></svg>Full time</span>
      </div>
      <a class="apply-button" href="#">Apply</a>
    </div>
    <div class="job-row">
      <h4>Logistics Manager - Fashion Retail</h4>
      <div class="job-meta">
        <span><svg><use href="#pin"/></svg>Singapore</span>
        <span><svg><use href="#chat"/></svg>Logistics</span>
        <span><svg><use href="#hourglass"/></svg>Full time</span>
      </div>
      <a class="apply-button" href="#">Apply</a>
    </div>
    <div class="job-row">
      <h4>IS Support Analyst, APAC</h4>
      <div class="job-meta">
        <span><svg><use href="#pin"/></svg>Singapore</span>
        <span><svg><use href="#chat"/></svg>Information Technology</span>
        <span><svg><use href="#hourglass"/></svg>Full time</span>
      </div>
      <a class="apply-button" href="#">Apply</a>
    </div>
  </div>
</section>

</body>
</html>
```